Letterhead design for a vibrant telco business using our wonderful logo

We need an elegant and captivating letterhead design that takes advantage of our bright and colourful logo and reflects our brand name "Copper Wharf".
We are positioned as a fresh, vibrant and innovative VoIP carrier servicing the business market in Australia
We have a great website design that's flowed through to existing business card design. I can supply the CMYK colour details and font details as required.
There will be several other design jobs following this one for our brand.
Target Market(s)
Standard business correspondence. Mostly will be PDF'ing documents, some physical colour printing.
Industry/Entity Type
Telecommunications

```html
<!DOCTYPE html>
<html lang="en">
<head>
<meta charset="utf-8">
<title>Copper Wharf Letterhead</title>
<link rel="stylesheet" href="https://fonts.googleapis.com/css2?family=Open+Sans:wght@400;700&display=swap">
<style>
  :root {
    --paper: #ffffff;
    --ink: #4a4a4a;
    --brand-dark: #3d3d3f;
    --brand-mark: #ef8a3c;
    --tone-yellow: #f6dfa3;
    --tone-peach: #f5c9a5;
    --tone-pink: #f0b0b6;
    --tone-lavender: #cdb6da;
    --tone-blue: #a9cbe6;
    --tone-mint: #b4dfbf;
  }
  * { margin: 0; padding: 0; box-sizing: border-box; }
  html, body { width: 900px; height: 1200px; overflow: hidden; background: var(--paper); }
  .letterhead {
    position: relative;
    width: 900px;
    height: 1200px;
    background: var(--paper);
    font-family: "Open Sans", Arial, sans-serif;
    color: var(--ink);
  }
  .brand {
    position: absolute;
    top: 54px;
    right: 42px;
    display: flex;
    align-items: center;
    gap: 14px;
  }
  .brand-square {
    width: 64px;
    height: 64px;
    background: var(--brand-mark);
  }
  .brand-name {
    font-weight: 700;
    font-size: 34px;
    line-height: 1.02;
    letter-spacing: 0.5px;
    color: var(--brand-dark);
    text-transform: uppercase;
  }
  .graphic-area {
    position: absolute;
    left: 0;
    top: 0;
    width: 900px;
    height: 1200px;
  }
  .contact-line {
    position: absolute;
    left: 148px;
    top: 1100px;
    display: flex;
    gap: 42px;
    font-size: 14px;
    color: var(--ink);
  }
  .contact-line b { font-weight: 700; margin-right: 6px; }
</style>
</head>
<body>
  <div class="letterhead">
    <svg class="graphic-area" viewBox="0 0 900 1200" role="img" aria-label="Decorative pastel graphic rising from the lower left corner">
      <defs>
        <linearGradient id="pastelWash" x1="0" y1="1200" x2="900" y2="1100" gradientUnits="userSpaceOnUse">
          <stop offset="0" stop-color="var(--tone-mint)"/>
          <stop offset="0.15" stop-color="var(--tone-blue)"/>
          <stop offset="0.32" stop-color="var(--tone-lavender)"/>
          <stop offset="0.52" stop-color="var(--tone-pink)"/>
          <stop offset="0.75" stop-color="var(--tone-peach)"/>
          <stop offset="1" stop-color="var(--tone-yellow)"/>
        </linearGradient>
      </defs>
      <polygon fill="url(#pastelWash)" opacity="0.85" points="0,729 900,1125 900,1200 0,1200"/>
    </svg>

    <header class="brand">
      <div class="brand-square"></div>
      <div class="brand-name">Copper<br>Wharf</div>
    </header>

    <footer class="contact-line">
      <span><b>M</b>0400 123 456</span>
      <span><b>P</b>1300 555 010</span>
      <span><b>F</b>1300 555 012</span>
      <span>www.copperwharf.com.au</span>
    </footer>
  </div>
</body>
</html>
```